Motor Vehicle Wholesale Business Card design

I will be buying and selling cars throughout the motor car industry. I will be purchasing cars from one yard and wholesaling these cars to other motor car retailers. I am open to designs. I would think a car would be required within the logo, and generally the cars are mainstream cars. Please do not use prestige cars in the logo.If not a car in the logo, then i am open to designs that do also indicate this as well.

This is not a retail business, just wholesale only.

Thanks

Target Market(s)

car dealers/dealerships

Industry/Entity Type

Retail

Contact Information for Business Card

KVL Wholesale
Colin Hartwell
Mob: 0438207164

Requirements
Must have
• A picture of a car or a representation of a car is required as i am dealing in the motor vehicle industry.

```html
<!DOCTYPE html>
<html lang="en">
<head>
<meta charset="utf-8">
<title>KVL Wholesale – Business Card</title>
<link rel="stylesheet" href="https://fonts.googleapis.com/css2?family=Mulish:wght@300;400;800&display=swap">
<style>
  :root {
    --backdrop: #e4e4e4;
    --card: #ffffff;
    --card-edge: #efefef;
    --ink: #2b2b2b;
    --ink-soft: #4a4a4a;
    --red-light: #d3202a;
    --red-mid: #b5161f;
    --red-dark: #8c0f17;
    --band-text: #ffffff;
  }
  * { margin: 0; padding: 0; box-sizing: border-box; }
  html, body {
    width: 1200px;
    height: 862px;
    overflow: hidden;
    background: var(--backdrop);
    font-family: "Mulish", sans-serif;
  }
  .canvas {
    position: relative;
    width: 1200px;
    height: 862px;
  }
  .business-card {
    position: absolute;
    left: 110px;
    top: 151px;
    width: 980px;
    height: 560px;
    background: radial-gradient(ellipse at 55% 35%, var(--card) 0%, var(--card-edge) 100%);
    box-shadow: 0 6px 24px rgba(0,0,0,0.12);
  }
  .brand {
    position: absolute;
    left: 64px;
    top: 66px;
    display: flex;
    align-items: center;
    gap: 10px;
  }
  .brand-dot {
    width: 16px;
    height: 16px;
    border-radius: 50%;
    background: var(--red-light);
  }
  .brand-name {
    font-weight: 800;
    font-size: 30px;
    line-height: 1;
    letter-spacing: 1px;
    color: var(--red-light);
    text-transform: uppercase;
  }
  .holder-name {
    position: absolute;
    right: 70px;
    top: 72px;
    font-weight: 800;
    font-size: 16px;
    letter-spacing: 0.5px;
    color: var(--ink);
    text-transform: uppercase;
  }
  .address-band {
    position: absolute;
    left: 0;
    right: 0;
    top: 180px;
    height: 150px;
    background: linear-gradient(180deg, var(--red-light) 0%, var(--red-mid) 55%, var(--red-dark) 100%);
    display: flex;
    align-items: center;
    justify-content: center;
  }
  .address {
    color: var(--band-text);
    font-weight: 300;
    font-size: 33px;
  }
  .contact-row {
    position: absolute;
    left: 60px;
    right: 50px;
    bottom: 46px;
    display: flex;
    justify-content: space-between;
    font-size: 17px;
    color: var(--ink-soft);
  }
  .contact-label {
    font-weight: 800;
    color: var(--ink);
  }
</style>
</head>
<body>
<main class="canvas">
  <section class="business-card">
    <div class="brand">
      <span class="brand-dot"></span>
      <span class="brand-name">KVL Wholesale</span>
    </div>
    <p class="holder-name">Colin Hartwell</p>
    <div class="address-band">
      <p class="address">2715 Harbor Road, Suite 204 Riverton, NJ 08077</p>
    </div>
    <div class="contact-row">
      <p><span class="contact-label">Mob:</span> 0438207164</p>
      <p><span class="contact-label">Fax No:</span> 0438207164</p>
      <p><span class="contact-label">LMCT:</span> 0438207164</p>
      <p><span class="contact-label">ABN:</span> 0438207164</p>
      <p><span class="contact-label">ACN:</span> 0438207164</p>
    </div>
  </section>
</main>
</body>
</html>
```